Visual design for database driven web application

Need a clean, professional looking visual design for a web application.

PLUME is the new standardized K-12 school testing program for the state of Texas. We are building an application named PLUME-Finder (clever, yeah?) that will allow teachers, school administrators, and others to EASILY sort through millions of records of student data and print or export reports showing just the information they need about their students.

The state currently doesn't provide a user-friendly way to do this. They provide a "data dump" spreadsheet that school administrators and teachers must figure out how to manipulate to get the data they need. We are building a Web-based tool that will make it super simple and easy for our users to get the data they need in a format that works for them.

I've created a basic wireframe of the main application screen in Vellum QD Max. I need you to "skin" the wireframe to make it look good. Your mockup will set the tone for branding and visual design throughout the site.

See the attached screenshots. There are a few variations of the screen that include dynamic panels that open & close. Start by designing just the main screen and if you have time, do one or two of the panels. Thanks!
Updates

Target Market(s)

K-12 education professionals (teachers, administrators) in the state of Texas

Industry/Entity Type

Building

Requirements
Must have
• Your mockups should include all of the features & content shown in the attached screenshots.

However, you don't have to show all 10 rows of data. You can just do the column headers and one row of data. (It would be repetitive and unnecessary to spend time re-creating the entire grid with all of that data just to show your visual styling.)

The design should reflect the following concepts:

- Texas
- Education
- Simplicity
- Helpfulness
- Trust
- Professionalism

If I select your design, I will want your design source files (Illustrator, Photoshop, etc.)
Nice to have
• A logo in the upper left corner for PLUME-Finder. The logo should definitely communicate the design concepts described under "must have."

```html
<!DOCTYPE html>
<html lang="en">
<head>
<meta charset="utf-8">
<title>PLUME-Finder</title>
<link rel="stylesheet" href="https://fonts.googleapis.com/css2?family=Open+Sans:wght@400;600;700&display=swap">
<style>
:root{
  --bg-top:#1aa1b6;
  --bg-bottom:#2cb6cd;
  --rule:#a9dbe3;
  --logo:#e9f7f9;
  --ink:#1d2b2e;
  --teal-text:#1b8fa3;
  --teal-dark:#1aa3b8;
  --panel:#f1fafb;
  --head-cell:#b7dfe6;
  --row-alt:#cdeef3;
  --row-text:#2a9db0;
  --check-btn:#d8f0a7;
  --cancel:#afd070;
  --apply:#88e2dc;
  --pager:#a6dfe8;
  --pager-btn:#e6f5f8;
  --field:#4cb8c9;
}
*{box-sizing:border-box;margin:0;padding:0}
html,body{width:1200px;height:803px;overflow:hidden}
body{background:linear-gradient(var(--bg-top),var(--bg-bottom));font-family:"Open Sans",Arial,sans-serif}
.stage{position:absolute;left:0;top:0;width:1024px;height:685px;transform:scale(1.171875);transform-origin:0 0}
.abs{position:absolute}
.header-rule{left:0;top:122px;width:1024px;height:5px;background:var(--rule)}
.logo{left:60px;top:51px;font-family:"Open Sans",Arial,sans-serif;font-weight:700;font-size:30px;color:var(--logo)}
.welcome{left:507px;top:27px;font-size:12.5px;color:var(--ink)}
.account{left:691px;top:28px;font-size:11px;font-weight:600;color:#cdeef2;letter-spacing:.8px;word-spacing:4px}
.tools{left:906px;top:19px;display:flex;gap:8px;align-items:center}
.tools .sep{width:1px;height:16px;background:#8fd2dc}
.search-field{left:692px;top:62px;width:216px;height:27px;background:var(--field);border:1px solid #2a8391}
.search-field svg{position:absolute;right:-2px;top:0}
.search-btn{left:917px;top:65px;width:78px;height:15px;border-radius:3px;background:#40c6e0;color:#fff;font-weight:700;font-size:12.5px;line-height:15px;text-align:center}
.search-option{left:788px;top:91px;font-size:11px;color:#d6f2f6;display:flex;gap:4px;align-items:center}
.tab{top:166px;width:175px;height:30px;font-size:15px;line-height:31px;text-align:center}
.tab-active{left:90px;background:linear-gradient(#18c8f0,#1aa9cf);color:#fff}
.tab-idle{left:285px;background:#2898a7;color:#d4eff4}
.main-panel{left:31px;top:196px;width:966px;height:387px;background:var(--panel);border-radius:3px}
.grid-head,.grid-row{position:absolute;left:45px;height:29px;font-size:12.5px;color:var(--row-text)}
.grid-head{top:216px;width:940px;height:28px;background:var(--head-cell);color:var(--ink)}
.grid-row.alt{background:var(--row-alt)}
.grid-row.strong{font-weight:700;color:#278fa0}
.cell{position:absolute;top:7px;white-space:nowrap}
.grid-head .cell{top:6px}
.dialog{left:42px;top:209px;width:656px;height:312px;background:var(--panel);border:6px solid var(--teal-dark)}
.dialog-bar{position:absolute;left:0;top:4px;width:644px;height:40px;background:#fbfeff;border-bottom:2px solid var(--teal-dark);font-size:12.5px;color:var(--teal-text)}
.dialog-bar span{position:absolute;top:12px}
.bulk-btn{position:absolute;top:54px;width:122px;height:23px;background:var(--check-btn);font-size:13px;color:#3a4a2a;text-align:center;line-height:24px}
.bulk-rule{position:absolute;left:0;top:78px;width:644px;height:1px;background:#cfe6ea}
.option{position:absolute;display:flex;align-items:center;gap:10px;font-size:12.5px;color:#3b4648}
.option i{width:12px;height:12px;border:1px solid #7f8b8d;background:#fff;box-shadow:inset 1px 1px 1px #bbb}
.action{position:absolute;top:267px;height:25px;font-size:13px;font-weight:700;text-align:center;line-height:25px}
.action.cancel{left:409px;width:97px;background:var(--cancel);color:#1f2a10}
.action.apply{left:511px;width:95px;background:var(--apply);color:#46612c;border-radius:2px}
.pager{left:32px;top:592px;width:964px;height:41px;background:var(--pager);border-radius:4px;font-size:13px}
.pager .label{position:absolute;left:37px;top:14px;color:var(--ink)}
.pager .label b{font-weight:400}
.pager .label em{font-style:normal;color:#6fb8c5}
.pager-btn{position:absolute;top:12px;width:93px;height:22px;background:var(--pager-btn);font-weight:700;color:#4b6d74;text-align:center;line-height:22px}
.pager .show{position:absolute;left:753px;top:13px;font-weight:700;color:var(--teal-text)}
.pager .per-page{position:absolute;left:805px;top:9px;width:73px;height:25px;background:#c6e9ef;border-radius:2px;font-weight:700;color:#2f4548;padding-left:15px;line-height:25px}
.pager .per-page svg{position:absolute;right:8px;top:2px}
</style>
</head>
<body>
<div class="stage">
  <div class="abs header-rule"></div>
  <div class="abs logo">PLUME-Finder</div>
  <div class="abs welcome">Welcome &nbsp;: Dana</div>
  <div class="abs account">My Profile &nbsp;/ Logout</div>
  <div class="abs tools">
    <svg width="20" height="18" viewBox="0 0 20 18" aria-label="Print"><rect x="5" y="1" width="10" height="6" fill="#fff"/><rect x="1" y="6" width="18" height="8" rx="2" fill="#7fc77a"/><rect x="5" y="11" width="10" height="6" fill="#fff" stroke="#9aa" stroke-width=".6"/></svg>
    <span class="sep"></span>
    <svg width="16" height="18" viewBox="0 0 16 18" aria-label="Save"><rect x="1" y="1" width="14" height="16" rx="1" fill="#2d3b3e"/><rect x="4" y="1" width="8" height="6" fill="#e9eef0"/><rect x="4" y="11" width="8" height="6" fill="#f3c94a"/></svg>
  </div>
  <div class="abs search-field">
    <svg width="32" height="27" viewBox="0 0 32 27"><circle cx="14" cy="11" r="7" fill="none" stroke="#1d3438" stroke-width="2.5"/><line x1="19" y1="16" x2="27" y2="24" stroke="#1d3438" stroke-width="4" stroke-linecap="round"/></svg>
  </div>
  <div class="abs search-btn">Search</div>
  <div class="abs search-option">Search &nbsp;Option <svg width="20" height="12" viewBox="0 0 20 12"><path d="M1 1h18L10 11z" fill="none" stroke="#d6f2f6" stroke-width="1.3"/></svg></div>

  <div class="abs tab tab-active">Instructions</div>
  <div class="abs tab tab-idle">Sutent Data</div>

  <div class="abs main-panel"></div>

  <div class="grid-head">
    <span class="cell" style="left:10px">ID</span><span class="cell" style="left:77px">Gr</span><span class="cell" style="left:128px">Yr</span><span class="cell" style="left:175px">Local ID</span><span class="cell" style="left:274px">Campus</span><span class="cell" style="left:349px">School</span><span class="cell" style="left:459px">Last</span><span class="cell" style="left:554px">First</span><span class="cell" style="left:653px">MI</span>
    <span class="cell" style="left:673px;top:0;width:104px;height:28px;border-left:2px solid var(--panel);text-align:center;padding-top:6px">Student ID</span>
    <span class="cell" style="left:778px;top:0;width:58px;height:28px;border-left:2px solid var(--panel);text-align:center;padding-top:6px">Gender</span>
    <span class="cell" style="left:837px;top:0;width:103px;height:28px;border-left:2px solid var(--panel);text-align:center;padding-top:6px">DOB</span>
  </div>

  <div class="grid-row" style="top:250px;width:940px"><span class="cell" style="left:688px">1234546734</span><span class="cell" style="left:802px">F</span><span class="cell" style="left:853px">28/03/1980</span></div>
  <div class="grid-row alt" style="top:285px;width:934px"><span class="cell" style="left:688px">1234546734</span><span class="cell" style="left:802px">F</span><span class="cell" style="left:853px">28/03/1980</span></div>
  <div class="grid-row" style="top:316px;width:940px"><span class="cell" style="left:688px">1234546734</span><span class="cell" style="left:802px">F</span><span class="cell" style="left:853px">28/03/1980</span></div>
  <div class="grid-row alt" style="top:345px;width:940px"><span class="cell" style="left:688px">1234546734</span><span class="cell" style="left:802px">F</span><span class="cell" style="left:853px">28/03/1980</span></div>
  <div class="grid-row" style="top:374px;width:940px"><span class="cell" style="left:688px">1234546734</span><span class="cell" style="left:802px">F</span><span class="cell" style="left:853px">28/03/1980</span></div>
  <div class="grid-row alt strong" style="top:405px;width:940px;height:30px"><span class="cell" style="left:688px;font-weight:400;color:var(--row-text)">1234546734</span><span class="cell" style="left:802px">F</span><span class="cell" style="left:853px">28/03/1980</span></div>
  <div class="grid-row" style="top:435px;width:940px"><span class="cell" style="left:688px">1234546734</span><span class="cell" style="left:802px">F</span><span class="cell" style="left:853px">28/03/1980</span></div>
  <div class="grid-row alt" style="top:467px;width:940px;height:31px"><span class="cell" style="left:688px">1234546734</span><span class="cell" style="left:802px">F</span><span class="cell" style="left:853px">28/03/1980</span></div>
  <div class="grid-row" style="top:501px;width:940px">
    <span class="cell" style="left:12px">411</span><span class="cell" style="left:77px">9</span><span class="cell" style="left:130px">10</span><span class="cell" style="left:175px">9999999999</span><span class="cell" style="left:274px">Example</span><span class="cell" style="left:349px">Example H S</span><span class="cell" style="left:459px">Delgano</span><span class="cell" style="left:554px">MARISOL</span><span class="cell" style="left:651px">I</span><span class="cell" style="left:688px">1234546734</span><span class="cell" style="left:802px">F</span><span class="cell" style="left:853px">28/03/1980</span>
  </div>
  <div class="grid-row alt" style="top:533px;width:940px;height:30px">
    <span class="cell" style="left:12px">411</span><span class="cell" style="left:77px">9</span><span class="cell" style="left:130px">10</span><span class="cell" style="left:175px">9999999999</span><span class="cell" style="left:274px">Example</span><span class="cell" style="left:349px">Example H S</span><span class="cell" style="left:459px">Delgano</span><span class="cell" style="left:554px">MARISOL</span><span class="cell" style="left:651px">I</span><span class="cell" style="left:688px">1234546734</span><span class="cell" style="left:802px">F</span><span class="cell" style="left:853px">28/03/1980</span>
  </div>

  <div class="abs dialog">
    <div class="dialog-bar">
      <span style="left:13px">Showing 26 of 38 Columns</span>
      <span style="left:249px;display:flex;align-items:center;gap:9px">Show / Hide Columns <svg width="13" height="10" viewBox="0 0 13 10"><path d="M0 0h13L6.5 10z" fill="#1d2b2e"/></svg></span>
      <span style="left:492px">3 Colums are Filitered</span>
    </div>
    <div class="bulk-btn" style="left:9px">Check all</div>
    <div class="bulk-btn" style="left:142px">uncheck all</div>
    <div class="bulk-rule"></div>

    <div class="option" style="left:30px;top:97px"><i></i>Date</div>
    <div class="option" style="left:152px;top:97px"><i></i>Gender</div>
    <div class="option" style="left:291px;top:97px"><i></i>TI</div>
    <div class="option" style="left:404px;top:97px"><i></i>Fall CDC</div>
    <div class="option" style="left:30px;top:125px"><i></i>Date</div>
    <div class="option" style="left:152px;top:125px"><i></i>Gender</div>
    <div class="option" style="left:291px;top:125px"><i></i>TI</div>
    <div class="option" style="left:404px;top:125px"><i></i>Fall CDC</div>
    <div class="option" style="left:30px;top:152px"><i></i>Date</div>
    <div class="option" style="left:152px;top:152px"><i></i>Gender</div>
    <div class="option" style="left:291px;top:152px"><i></i>TI</div>
    <div class="option" style="left:404px;top:152px"><i></i>Fall CDC</div>
    <div class="option" style="left:30px;top:180px"><i></i>Date</div>
    <div class="option" style="left:152px;top:180px"><i></i>Gender</div>
    <div class="option" style="left:291px;top:180px"><i></i>TI</div>
    <div class="option" style="left:404px;top:180px"><i></i>Fall CDC</div>
    <div class="option" style="left:30px;top:208px"><i></i>Date</div>
    <div class="option" style="left:152px;top:208px"><i></i>Gender</div>
    <div class="option" style="left:291px;top:208px"><i></i>TI</div>
    <div class="option" style="left:404px;top:208px"><i></i>Fall CDC</div>
    <div class="option" style="left:30px;top:236px"><i></i>Date</div>
    <div class="option" style="left:152px;top:236px"><i></i>Gender</div>
    <div class="option" style="left:291px;top:236px"><i></i>TI</div>
    <div class="option" style="left:404px;top:236px"><i></i>Fall CDC</div>

    <div class="action cancel">Cancel</div>
    <div class="action apply">Apply</div>
  </div>

  <div class="abs pager">
    <span class="label">Page : &nbsp;<b>1</b> <em>2 3 4.......25</em></span>
    <div class="pager-btn" style="left:229px">Next</div>
    <div class="pager-btn" style="left:335px">Previous</div>
    <span class="show">Show</span>
    <div class="per-page">10
      <svg width="20" height="21" viewBox="0 0 20 21"><path d="M10 1l9 8H1z" fill="#3f5a5e"/><path d="M10 20l9-8H1z" fill="#3f5a5e"/></svg>
    </div>
  </div>
</div>
</body>
</html>
```